Dolsemk Business Cards

Business cards for real estate
Target Market(s)
Real estate
Industry/Entity Type
Real Estate Agent
Font styles to use
Serif
Requirements
Must have
- Photo and logo

```html
<!DOCTYPE html>
<html lang="en">
<head>
<meta charset="utf-8">
<title>Dolsemk Realty Business Card</title>
<link rel="stylesheet" href="https://fonts.googleapis.com/css2?family=Cinzel:wght@500;600&family=Lora:wght@400&display=swap">
<style>
  :root {
    --page: #e9e6e2;
    --card-top-a: #f7f7f8;
    --card-top-b: #dcdde0;
    --maroon: #6e2027;
    --maroon-dark: #4e151a;
    --ink: #1b1416;
    --panel-a: #2a2526;
    --panel-b: #0f0d0e;
    --gold: #c7a470;
    --cream: #ebe3da;
    --photo-a: #3a3b44;
    --photo-b: #15161c;
  }
  html, body {
    margin: 0;
    width: 1200px;
    height: 970px;
    overflow: hidden;
    background: var(--page);
  }
  .card {
    position: absolute;
    left: 80px;
    top: 188px;
    width: 1040px;
    height: 594px;
    border-radius: 28px;
    overflow: hidden;
    background: linear-gradient(180deg, var(--card-top-a), var(--card-top-b));
    box-shadow: 0 18px 40px rgba(0,0,0,.25);
    font-family: "Lora", serif;
  }
  .brand {
    position: absolute;
    left: 60px;
    top: 98px;
    display: flex;
    align-items: center;
    gap: 28px;
  }
  .brand-mark {
    width: 92px;
    height: 92px;
    background: var(--maroon);
  }
  .brand-name {
    font-family: "Cinzel", serif;
    font-weight: 600;
    color: var(--ink);
    line-height: 1;
    font-size: 54px;
    letter-spacing: 2px;
  }
  .brand-name span { display: block; font-size: 44px; letter-spacing: 9px; margin-top: 8px; }
  .name-band {
    position: absolute;
    left: 0; top: 325px;
    width: 100%; height: 53px;
    background: linear-gradient(180deg, var(--maroon), var(--maroon-dark));
    display: flex;
    align-items: center;
    padding-left: 58px;
    box-sizing: border-box;
    color: var(--cream);
  }
  .person-name { font-size: 32px; letter-spacing: 1px; }
  .divider { width: 2px; height: 30px; background: var(--cream); margin: 0 20px; opacity: .8; }
  .person-role { font-size: 23px; letter-spacing: .5px; }
  .details {
    position: absolute;
    left: 0; top: 378px;
    width: 100%; height: 216px;
    background: linear-gradient(180deg, var(--panel-a), var(--panel-b));
  }
  .address {
    position: absolute;
    left: 58px; top: 20px;
    color: var(--cream);
    font-size: 24px;
    line-height: 33px;
    margin: 0;
  }
  .contact {
    position: absolute;
    left: 58px;
    display: flex;
    align-items: center;
    gap: 12px;
    color: var(--cream);
    font-size: 24px;
  }
  .contact.phone { top: 100px; }
  .contact.email { top: 140px; }
  .contact svg { width: 30px; height: 30px; }
  .portrait {
    position: absolute;
    left: 560px; top: 40px;
    width: 440px; height: 554px;
    background: radial-gradient(ellipse at 50% 35%, var(--photo-a), var(--photo-b) 75%);
    border-radius: 200px 200px 0 0;
  }
</style>
</head>
<body>
  <div class="card">
    <div class="brand">
      <div class="brand-mark"></div>
      <div class="brand-name">Dolsemk<span>Realty</span></div>
    </div>

    <div class="name-band">
      <span class="person-name">MARK ELLERY</span>
      <span class="divider"></span>
      <span class="person-role">Director</span>
    </div>

    <div class="details">
      <p class="address">PO BOX 482, Kestrel Road<br>9th street, Westbrook</p>
      <div class="contact phone">
        <svg viewBox="0 0 30 30" aria-hidden="true">
          <circle cx="15" cy="15" r="13" fill="none" stroke="var(--gold)" stroke-width="2"/>
          <rect x="11" y="8" width="8" height="14" rx="1.5" fill="none" stroke="var(--gold)" stroke-width="1.8"/>
          <line x1="13.5" y1="19.5" x2="16.5" y2="19.5" stroke="var(--gold)" stroke-width="1.5"/>
        </svg>
        <span>(555) 804 3162</span>
      </div>
      <div class="contact email">
        <svg viewBox="0 0 30 30" aria-hidden="true">
          <circle cx="15" cy="15" r="13" fill="none" stroke="var(--gold)" stroke-width="2"/>
          <rect x="8.5" y="10" width="13" height="10" fill="var(--gold)"/>
          <polyline points="8.5,10 15,15.5 21.5,10" fill="none" stroke="var(--panel-b)" stroke-width="1.5"/>
        </svg>
        <span>info@dolsemkrealty.com</span>
      </div>
    </div>

    <div class="portrait" role="img" aria-label="Portrait photo of the director in a dark suit and blue tie, hands clasped"></div>
  </div>
</body>
</html>
```